Quarrow financial services, is a financial company that provides consultancy, brokerage services, and funding.

we will be providing the clients with insights, knowledge and data with regards to the financial markets.

with the brokerage services we will try to find the suitable counterparts that provide them with the best investments that suits their needs and expected return.

Target Market(s)

financial institutions, Corporates, high-net worth individuals

Industry/Entity Type

Financial Service

Contact Information for Business Card

Font styles to use
Other font styles liked:
• applemyungjo

Colors
00a990
848484

Requirements
Must have
• the logo at the back
Nice to have
• Finesse
Should not have
• boldness

```html
<!DOCTYPE html>
<html lang="en">
<head>
<meta charset="utf-8">
<title>Quarrow Financial Services – Business Card</title>
<link rel="stylesheet" href="https://fonts.googleapis.com/css2?family=Cinzel:wght@400&family=Arimo:wght@400&family=Cormorant+Garamond:ital,wght@1,400&display=swap">
<style>
  :root {
    --backdrop: #d9d6d2;
    --card: #151617;
    --card-edge: #1d1e20;
    --gloss: #3a3b3e;
    --gloss-soft: #2e2f32;
    --accent: #7fae3f;
    --text-light: #e8e8e8;
    --divider: #5a5b5e;
    --logo-pale: #d6dccb;
    --logo-grey: #c9cacb;
  }
  * { box-sizing: border-box; margin: 0; padding: 0; }
  html, body {
    width: 1200px; height: 864px; overflow: hidden;
    background: var(--backdrop);
  }
  .canvas { position: relative; width: 1200px; height: 864px; }

  .card {
    position: absolute;
    width: 520px; height: 298px;
    background: var(--card);
    border: 1px solid var(--card-edge);
    box-shadow: 0 10px 28px rgba(0,0,0,.25);
  }

  /* Front */
  .card--front { left: 60px; top: 110px; }
  .front-brand {
    position: absolute; left: 0; right: 0; top: 58px;
    text-align: center; color: var(--gloss);
  }
  .front-mark {
    display: inline-block; width: 34px; height: 34px;
    background: var(--gloss-soft); margin-bottom: 14px;
  }
  .front-name {
    font-family: "Cinzel", serif; font-size: 44px; letter-spacing: 3px;
    line-height: 1;
  }
  .front-sub {
    font-family: "Cinzel", serif; font-size: 14px; letter-spacing: 4px;
    margin-top: 6px;
  }
  .front-tagline {
    font-family: "Cormorant Garamond", serif; font-style: italic;
    font-size: 14px; margin-top: 4px;
  }
  .front-web {
    position: absolute; left: 0; right: 0; bottom: 40px; text-align: center;
    font-family: "Cinzel", serif; font-size: 13px; letter-spacing: 4px;
    color: var(--gloss);
  }

  /* Back */
  .card--back { left: 620px; top: 456px; }
  .back-logo {
    position: absolute; left: 40px; top: 104px; width: 190px;
    display: flex; align-items: center; gap: 10px;
  }
  .back-logo-square { width: 22px; height: 22px; background: var(--accent); flex: none; }
  .back-logo-name {
    font-family: "Arimo", sans-serif; font-size: 30px; color: var(--logo-pale);
    letter-spacing: 1px;
  }
  .back-divider {
    position: absolute; left: 246px; top: 52px; width: 1px; height: 194px;
    background: linear-gradient(var(--card), var(--divider) 30%, var(--divider) 70%, var(--card));
  }
  .back-contact {
    position: absolute; left: 268px; top: 62px;
    font-family: "Arimo", sans-serif; color: var(--text-light);
  }
  .contact-name { font-size: 20px; color: var(--accent); line-height: 1.1; }
  .contact-role { font-size: 15px; margin-bottom: 12px; }
  .contact-address { font-size: 13px; line-height: 1.35; margin-bottom: 10px; }
  .contact-list { list-style: none; font-size: 13.5px; }
  .contact-list li { display: flex; align-items: center; gap: 8px; height: 21px; }
  .contact-list svg { width: 13px; height: 13px; flex: none; }
  .contact-list .no-icon { padding-left: 21px; }
</style>
</head>
<body>
<main class="canvas">

  <section class="card card--front" aria-label="Business card front">
    <div class="front-brand">
      <span class="front-mark"></span>
      <div class="front-name">QUARROW</div>
      <div class="front-sub">FINANCIAL SERVICES</div>
      <div class="front-tagline">Your Financial Partner</div>
    </div>
    <div class="front-web">WWW.QUARROWFS.COM</div>
  </section>

  <section class="card card--back" aria-label="Business card back">
    <div class="back-logo">
      <span class="back-logo-square"></span>
      <span class="back-logo-name">Quarrow</span>
    </div>
    <div class="back-divider"></div>
    <div class="back-contact">
      <div class="contact-name">Marcus Hale</div>
      <div class="contact-role">President</div>
      <div class="contact-address">2217 Alder Crest Lane<br>Brookvale, NY 11420</div>
      <ul class="contact-list">
        <li>
          <svg viewBox="0 0 16 16" aria-hidden="true"><path fill="#7fae3f" d="M2 5c0-2 2-3 6-3s6 1 6 3v1h-3V5H5v1H2zM4 7h8l2 7H2z"/><circle cx="8" cy="10.5" r="1.8" fill="#151617"/></svg>
          <span>555 0148 2290</span>
        </li>
        <li>
          <svg viewBox="0 0 16 16" aria-hidden="true"><rect x="1" y="3" width="14" height="10" fill="#7fae3f"/><path d="M1 3l7 6 7-6" fill="none" stroke="#151617" stroke-width="1.4"/></svg>
          <span>marcus@quarrowfs.com</span>
        </li>
        <li>
          <svg viewBox="0 0 16 16" aria-hidden="true"><circle cx="8" cy="8" r="7" fill="#7fae3f"/><circle cx="8" cy="6.5" r="2.2" fill="#151617"/><path d="M4.5 12c1-2 6-2 7 0" fill="#151617"/></svg>
          <span>www.quarrowfs.com</span>
        </li>
      </ul>
    </div>
  </section>

</main>
</body>
</html>
```